Product Catalog Redesign for Industrial Tools & PPE

1. Project Title:
Professional Product Catalog Redesign for Industrial Tools & Personal Protective Equipment (PPE)
2. Company Background:
We are a supplier of a wide range of industrial tools, equipment, and Personal Protective Equipment (PPE). Our target audience consists of professionals, technicians, and businesses in the construction, manufacturing, and agricultural sectors. We are known for our comprehensive product range and practical solutions.
3. Project Objective:
The primary goal is to redesign our existing product catalog. The new design must be professional, clean, modern, and highly user-friendly. It should project an image of trustworthiness and practicality, serving as an essential tool for our B2B customers to easily find and order products.
4. Key Requirements & Design Guidelines:
Ease of Future Editing (Crucial Requirement):
The final design must be created using simple, standard, and easily accessible fonts (e.g., from Google Fonts or Adobe Fonts library).
The source file must be perfectly organized, with clearly named layers and structured content. Our in-house team, which has basic design knowledge, must be able to easily make future changes, such as adding/removing products or updating prices, without needing advanced design skills in an editable PDF file.
Layout & Readability:
The layout must be clean, organized, and easy to navigate. Readability is a top priority.
To manage printing costs, we DO NOT want a "one product per page" design. The ideal layout should accommodate 4 to 6 products per page while maintaining a clean and uncluttered look.
A consistent grid system should be used throughout the catalog. Each product entry should have a clear hierarchy for: Product Title, Product Code/SKU, a brief description/specs, and an image.
Look & Feel:
Professional & Trustworthy: The design should feel reliable and targeted toward professionals. Avoid overly flashy or "retail flyer" aesthetics.
Practical & Functional: The design should prioritize function over excessive ornamentation. It is a tool for our customers, not a piece of art.
Modern & Clean: We want to move away from our outdated look towards a more contemporary and fresh design.
5. Catalog Structure & Categorization:
The catalog must be organized into the following specific product categories. We recommend using a clear visual system (e.g., color-coding, distinct section dividers) to separate them.
Consumables - Accessories
Welding
Grinding
Sawing
Personal Protective Equipment (PPE)
Hand Tools
Painting & Construction Tools
Garden - Agriculture
Fastening & Storage
Electrical Supplies
Chemicals - Cleaning - Household Goods
6. Materials We Will Provide:
File 1 - Current Catalog (PDF): This file contains all the up-to-date products, images, and text content that must be included in the new design. Please use this as the primary source for content. All text must be copied from this file in greek.
File 2 - Old Catalog (PDF): This is an old catalog. Its content is outdated and must NOT be used. We are providing it ONLY as a structural reference for a layout we previously liked. It can serve as a loose inspiration for structure, but you are free to propose better solutions.
Please find all relevant files in this link
https://filevault.example/share/folders/7QxkTr2LmWp9ZvNcAe--HjsduR_oK4T?src=share_link
7. Final Deliverables:
Editable Source File: A fully editable and perfectly organized source file. Adobe InDesign (.indd) and an editable PDF file are preferred. All layers, paragraph styles, and character styles must be logically named and easy to understand.
Print-Ready File: A high-resolution, print-ready PDF, complete with bleed and crop marks.
Font Information: A list of all fonts used in the design.
In summary, we are looking for a designer who can deliver a clean, professional, and highly functional catalog that not only looks great but is also practical to print and easy for our team to maintain. We look forward to seeing your creative and practical design solutions.
Target Market(s)
Greek B2B customers
Industry/Entity Type
Industrial Tools and PPE

```html
<!DOCTYPE html>
<html lang="el">
<head>
<meta charset="UTF-8">
<title>Κατάλογος Προϊόντων – Εισαγωγή</title>
<link href="https://fonts.googleapis.com/css2?family=Noto+Sans:wght@400;500&display=swap" rel="stylesheet">
<style>
  :root {
    --backdrop: #e7e7e7;
    --page-dark: #1c1c1c;
    --page-dark-edge: #2a2a2a;
    --orange-deep: #c2410f;
    --orange-mid: #e8772e;
    --orange-light: #f2ad74;
    --gear-orange: #e98a47;
    --gear-shade: #c9561c;
    --ink-dark: #3b2a20;
    --text-light: #d8d8d8;
  }
  * { margin: 0; padding: 0; box-sizing: border-box; }
  html, body {
    width: 1200px; height: 900px; overflow: hidden;
    background: var(--backdrop);
    font-family: "Noto Sans", Arial, sans-serif;
  }
  .spread {
    position: absolute; left: 50px; top: 200px;
    width: 1100px; height: 500px;
    display: flex;
  }
  .page { position: relative; width: 550px; height: 500px; overflow: hidden; }

  .page--intro {
    background: linear-gradient(90deg, var(--page-dark) 0%, var(--page-dark-edge) 100%);
  }
  .gear-art { position: absolute; display: block; }
  .gear-art--large { left: 310px; top: 40px; }
  .gear-art--small { left: 460px; top: 265px; }

  .intro-text {
    position: absolute; left: 60px; top: 165px; width: 235px;
    color: var(--text-light); font-size: 8px; line-height: 1.5;
  }
  .intro-text p { margin-bottom: 6px; }
  .intro-text ul { list-style: none; margin-bottom: 8px; }
  .intro-text li { position: relative; padding-left: 12px; margin-bottom: 2px; }
  .intro-text li::before { content: "•"; position: absolute; left: 2px; }

  .page--quote {
    background: linear-gradient(100deg, var(--orange-deep) 0%, var(--orange-mid) 30%, var(--orange-light) 100%);
  }
  .gear-art--outline { left: 55px; top: 170px; }
  .quote {
    position: absolute; left: 222px; top: 196px; width: 320px;
    color: var(--ink-dark); font-size: 20px; line-height: 1.4; font-weight: 400;
    white-space: nowrap;
  }
  .quote-mark { position: absolute; font-size: 16px; line-height: 1; color: var(--ink-dark); }
  .quote-mark--open { left: 206px; top: 192px; }
  .quote-mark--close { left: 222px; top: 258px; }
</style>
</head>
<body>
  <main class="spread">
    <section class="page page--intro">
      <svg class="gear-art gear-art--large" width="200" height="200" role="img" aria-label="Πορτοκαλί απεικόνιση γραναζιού">
        <circle cx="100" cy="100" r="96" fill="var(--gear-orange)"/>
      </svg>
      <svg class="gear-art gear-art--small" width="110" height="110" role="img" aria-label="Μικρό πορτοκαλί γρανάζι">
        <circle cx="55" cy="55" r="52" fill="var(--gear-orange)"/>
      </svg>

      <div class="intro-text">
        <p>Σκοπός αυτού του νέου καταλόγου είναι να παίξει το ρόλο ενός αναλυτικού οδηγού αγοράς. Χωρισμένος σε 11 κύριες προϊοντικές κατηγορίες, σχεδιάστηκε με τέτοιο τρόπο ώστε να:</p>
        <ul>
          <li>Παρέχει λύσεις για τις καθημερινές ανάγκες της επιχείρησής σας.</li>
          <li>Είναι ένα εργαλείο ολοκληρωμένης πληροφόρησης, απλό και γρήγορο στη χρήση του.</li>
          <li>Διευκολύνει τη μακροχρόνια σχέση εμπιστοσύνης με τους συνεργάτες μας.</li>
        </ul>
        <p>Στόχος μας είναι να προσφέρουμε πάντα υποδειγματικές υπηρεσίες και εξαιρετικά προϊόντα. Οι συνεργάτες μας ξέρουν ότι μπορούν να στηριχτούν σε εμάς επειδή:</p>
        <ul>
          <li>Τηρούμε τις δεσμεύσεις και τις συμφωνίες μας.</li>
          <li>Πάντα προσπαθούμε να βρούμε τρόπους για να ανταποκριθούμε στις ανάγκες σας.</li>
          <li>Εξελισσόμαστε συνεχώς για την καλύτερη εξυπηρέτηση και την ανάπτυξη της επιχείρησής σας.</li>
        </ul>
      </div>
    </section>

    <section class="page page--quote">
      <svg class="gear-art gear-art--outline" width="140" height="140" role="img" aria-label="Περίγραμμα γραναζιού σε σκούρο τόνο">
        <circle cx="70" cy="70" r="66" fill="var(--gear-shade)"/>
      </svg>
      <span class="quote-mark quote-mark--open">“</span>
      <blockquote class="quote">Η επιτυχία των πελατών μας είναι<br>η φιλοσοφία που μας οδηγεί.</blockquote>
      <span class="quote-mark quote-mark--close">”</span>
    </section>
  </main>
</body>
</html>
```